BuildLinkage.com Full Stationery Design

Business Card will have all info on it. Letterhead will not have name, title or mobile number. Keep general feeling very clean, using colors from the logo as accents.
Name:Dale Vanterpool
Title:President
Phone: 1-800-555-4926
Cell: 306-555-7312
email: dale@buildlinkage.com
website: www.buildlinkage.com
Address:
PO Box 874
Ridgeford, SK
S0M2T7

Target Market(s)

Construction Business owners

Industry/Entity Type

Business

Contact Information for Business Card

Name:Dale Vanterpool
Title:President
Phone: 1-800-555-4926
Cell: 306-555-7312
Address:
PO Box 874
Ridgeford, SK
S0M2T7

Font styles to use
Sans Serif

Requirements
Must have
• Clean look
Should not have
• Images or cartoon type characters or tools

```html
<!DOCTYPE html>
<html lang="en">
<head>
<meta charset="utf-8">
<title>BuildLinkage.com Letterhead</title>
<link href="https://fonts.googleapis.com/css2?family=Montserrat:wght@400;600&display=swap" rel="stylesheet">
<style>
  :root {
    --backdrop: #f1dcd8;
    --paper: #ffffff;
    --brand-orange: #e8620e;
    --brand-orange-deep: #e04e12;
    --brand-slate: #4f5966;
    --rule-grey: #d9dadc;
    --text-grey: #6b7078;
  }
  * { margin: 0; padding: 0; box-sizing: border-box; }
  html, body {
    width: 1200px;
    height: 784px;
    overflow: hidden;
    background: var(--backdrop);
  }
  .canvas {
    position: relative;
    width: 1200px;
    height: 784px;
  }
  .letterhead {
    position: absolute;
    left: 314px;
    top: 22px;
    width: 572px;
    height: 740px;
    background: var(--paper);
    overflow: hidden;
    box-shadow: 0 6px 18px rgba(150, 90, 80, 0.18);
    font-family: "Montserrat", sans-serif;
  }
  .edge-accent {
    position: absolute;
    width: 5px;
    height: 22px;
  }
  .edge-accent--slate { background: var(--brand-slate); opacity: 0.75; }
  .edge-accent--orange { background: var(--brand-orange); }
  .edge-accent.top-left.first { left: 0; top: 8px; }
  .edge-accent.top-left.second { left: 0; top: 30px; }
  .edge-accent.top-right.first { right: 0; top: 8px; }
  .edge-accent.top-right.second { right: 0; top: 30px; }

  .brand {
    position: absolute;
    left: 30px;
    top: 30px;
    display: flex;
    align-items: center;
    gap: 9px;
  }
  .brand-square {
    width: 22px;
    height: 22px;
    background: var(--brand-orange);
  }
  .brand-name {
    font-weight: 600;
    font-size: 17px;
    line-height: 1.05;
    color: var(--brand-slate);
    letter-spacing: 0.2px;
  }

  .contact {
    position: absolute;
    right: 26px;
    top: 32px;
    list-style: none;
    font-size: 6.5px;
    line-height: 10px;
    color: var(--text-grey);
    white-space: nowrap;
  }
  .contact li {
    display: flex;
    align-items: center;
    gap: 5px;
  }
  .contact-dot {
    width: 6px;
    height: 6px;
    border-radius: 50%;
    background: var(--brand-orange);
    flex: none;
  }

  .footer-wave {
    position: absolute;
    left: 0;
    bottom: 0;
    width: 572px;
    height: 200px;
  }
</style>
</head>
<body>
<main class="canvas">
  <article class="letterhead">
    <span class="edge-accent edge-accent--slate top-left first"></span>
    <span class="edge-accent edge-accent--orange top-left second"></span>
    <span class="edge-accent edge-accent--orange top-right first"></span>
    <span class="edge-accent edge-accent--slate top-right second"></span>

    <header class="brand">
      <span class="brand-square"></span>
      <span class="brand-name">BuildLinkage.com</span>
    </header>

    <ul class="contact">
      <li><span class="contact-dot"></span>PO Box 874, Ridgeford, SK, S0M2T7</li>
      <li><span class="contact-dot"></span>Phone: 1-800-555-4926</li>
      <li><span class="contact-dot"></span>dale@buildlinkage.com</li>
      <li><span class="contact-dot"></span>www.buildlinkage.com</li>
    </ul>

    <svg class="footer-wave" viewBox="0 0 572 200" aria-hidden="true">
      <defs>
        <linearGradient id="waveOrange" x1="0" y1="0" x2="1" y2="0">
          <stop offset="0" stop-color="var(--brand-orange-deep)"/>
          <stop offset="0.5" stop-color="var(--brand-orange)"/>
          <stop offset="1" stop-color="var(--brand-orange-deep)"/>
        </linearGradient>
      </defs>
      <path d="M0 30 C 160 30, 240 200, 572 196 L572 200 L0 200 Z" fill="url(#waveOrange)"/>
      <path d="M0 20 C 150 20, 250 186, 572 184 L572 194 C 250 194, 160 34, 0 34 Z" fill="var(--paper)"/>
      <path d="M0 24 C 150 24, 250 188, 572 186 L572 190 C 250 192, 152 30, 0 30 Z" fill="var(--rule-grey)"/>
      <path d="M0 12 C 140 12, 250 170, 572 176 L572 180 C 250 176, 140 18, 0 18 Z" fill="var(--brand-orange)"/>
    </svg>
  </article>
</main>
</body>
</html>
```